New Business Card Design Project

We are looking for a talented individual to create a truly awesome/unique business card design for us. We are looking for a someone to design something that will really stand out from the crowd - we don't mind what ideas you come up with (ie embossed/flat/matte/shine etc etc) just wow us with your creativity.
Updates

Sick

Target Market(s)

Video Games Industry Professionals (all levels of seniority from QA Testers through to CEOs)

Contact Information for Business Card

Company logo (see upload)
Company name: Northbridge Play Careers Ltd
Employee Name: Harriet Vasko
Job title: CEO
Website: www.npc2go.com
Office +44 1632 960418
Mobile: +44 7700 900582
Email: harriet@npc2go.com

Colors

Designer to choose colors to be used in the design.

Requirements
Must have
• The business card design MUST contain all the information listed in the BUSINESS CARD DETAILS box.
• You will see the colours that are relevant to us (ie company logo) in the uploaded imagery - however you do not have to use all these colours when designing the business card itself
• MUST BE DOUBLE SIDED

```html
<!DOCTYPE html>
<html lang="en">
<head>
<meta charset="utf-8">
<title>Northbridge Play Careers – Business Card</title>
<link rel="stylesheet" href="https://fonts.googleapis.com/css2?family=Montserrat:wght@500;600;700;800&display=swap">
<style>
  :root {
    --navy: #1f2d5e;
    --navy-deep: #232a66;
    --orange: #f07a1a;
    --white: #ffffff;
    --stage: #2b2c30;
    --crest: #c8cde0;
  }
  * { box-sizing: border-box; margin: 0; padding: 0; }
  html, body {
    width: 1200px; height: 800px; overflow: hidden;
    background: var(--stage);
    font-family: "Montserrat", Arial, sans-serif;
  }
  .canvas { position: relative; width: 1200px; height: 800px; }

  .card {
    position: absolute; left: 320px; width: 560px; height: 320px;
    overflow: hidden; box-shadow: 0 12px 30px rgba(0,0,0,.45);
  }
  .card--front { top: 50px; background: var(--navy); }
  .card--back  { top: 430px; background: var(--white); }

  .edge-tab {
    position: absolute; width: 20px; height: 145px;
    background: var(--orange); border: 2px solid var(--white);
    border-radius: 6px;
  }
  .card--front .edge-tab--right { right: -8px; top: 45px; }
  .card--front .edge-tab--left  { left: -8px; top: 105px; }
  .card--back  .edge-tab--left  { left: -8px; top: 95px; border-color: var(--white); }

  .brand {
    position: absolute; display: flex; align-items: center; gap: 14px;
  }
  .card--front .brand { left: 118px; top: 124px; }
  .brand__crest {
    width: 66px; height: 66px; border-radius: 50%; background: var(--crest); opacity: .9;
  }
  .brand__name {
    font-weight: 800; font-size: 27px; line-height: 1.05; color: var(--white);
    letter-spacing: .3px;
  }
  .card--back .brand { left: 60px; top: 205px; }
  .card--back .brand__name { color: var(--navy-deep); font-size: 24px; }

  .contact-panel {
    position: absolute; right: 0; top: 42px; width: 310px; height: 150px;
    background: var(--navy-deep); border-radius: 10px 0 0 10px;
    padding: 20px 18px 0 24px; color: var(--white);
  }
  .person__name { font-weight: 700; font-size: 20px; letter-spacing: .2px; }
  .person__role { font-weight: 600; font-size: 11px; color: var(--orange); margin-top: 1px; }
  .contact-panel__rule {
    position: absolute; left: 100px; right: 18px; top: 42px;
    height: 1.5px; background: var(--orange);
  }
  .company { font-weight: 600; font-size: 12px; color: var(--orange); margin-top: 8px; }
  .contact-list {
    display: grid; grid-template-columns: 1fr 1fr; gap: 6px 10px; margin-top: 10px;
    list-style: none; font-weight: 500; font-size: 10.5px;
  }
  .contact-list li { display: flex; align-items: center; gap: 6px; white-space: nowrap; }
  .contact-icon { width: 14px; height: 14px; flex: none; }
</style>
</head>
<body>
<main class="canvas">

  <section class="card card--front" aria-label="Card front">
    <span class="edge-tab edge-tab--right"></span>
    <span class="edge-tab edge-tab--left"></span>
    <div class="brand">
      <span class="brand__crest" role="img" aria-label="Company crest illustration"></span>
      <span class="brand__name">Northbridge<br>Play Careers</span>
    </div>
  </section>

  <section class="card card--back" aria-label="Card back">
    <span class="edge-tab edge-tab--left"></span>
    <div class="brand">
      <span class="brand__name">Northbridge<br>Play Careers</span>
    </div>

    <div class="contact-panel">
      <p class="person__name">Harriet Vasko</p>
      <p class="person__role">CEO</p>
      <span class="contact-panel__rule"></span>
      <p class="company">Northbridge Play Careers Ltd</p>
      <ul class="contact-list">
        <li>
          <svg class="contact-icon" viewBox="0 0 14 14" aria-hidden="true"><circle cx="7" cy="7" r="7" fill="#f07a1a"/><path d="M4.6 3.8l1.3-.3.7 1.6-.8.6c.4.9 1 1.5 1.9 1.9l.6-.8 1.6.7-.3 1.3c-3 .2-5.2-2-5-5z" fill="#fff"/></svg>
          +44 1632 960418
        </li>
        <li>
          <svg class="contact-icon" viewBox="0 0 14 14" aria-hidden="true"><circle cx="7" cy="7" r="7" fill="#f07a1a"/><rect x="3.6" y="4.6" width="6.8" height="4.8" rx=".6" fill="#fff"/><path d="M3.8 4.9L7 7.3l3.2-2.4" stroke="#f07a1a" stroke-width=".8" fill="none"/></svg>
          harriet@npc2go.com
        </li>
        <li>
          <svg class="contact-icon" viewBox="0 0 14 14" aria-hidden="true"><circle cx="7" cy="7" r="7" fill="#f07a1a"/><rect x="5" y="3.4" width="4" height="7.2" rx=".8" fill="#fff"/><circle cx="7" cy="9.5" r=".5" fill="#f07a1a"/></svg>
          +44 7700 900582
        </li>
        <li>
          <svg class="contact-icon" viewBox="0 0 14 14" aria-hidden="true"><circle cx="7" cy="7" r="7" fill="#f07a1a"/><circle cx="7" cy="7" r="3.4" fill="none" stroke="#fff" stroke-width=".9"/><ellipse cx="7" cy="7" rx="1.4" ry="3.4" fill="none" stroke="#fff" stroke-width=".8"/><path d="M3.6 7h6.8" stroke="#fff" stroke-width=".8"/></svg>
          www.npc2go.com
        </li>
      </ul>
    </div>
  </section>

</main>
</body>
</html>
```